Text heavy poster for university audience

I have developed a set of standards for online teaching that need to be turned into a post format. The project has a logo which should be incorporated. Most of the designing will be in terms of text layout. The logo (two versions - higher quality files available) and the a sample of standards (as image - word version available; the example is one third of standards) are attached. Design that can be adapted to brochure format would be great. (Brochure adaption will be paid separately via another project to be opened here). More details available here: http://www.brightmeadowhub.org
Updates

Dear all,

The URL for the site needs to be include in the design - either as footer or under logo:
<http://www.brightmeadowhub.org>

Sorry for late notice

Target Market(s)

The are university staff

Industry/Entity Type

University

Font styles to use
Serif
Sans Serif

Requirements
Must have
• The text in the "required" attachment must be included; but for initial draft feel free to restrict your design to "sample" attachment
The green from the Logo (PANTONE 17-5641 Emerald) should be the foundation of the colour palette.
Nice to have
• The collaborators as named here: http://www.brightmeadowhub.org/collaborators/
My preferred find is helvetica neue, but similar can be used
Should not have
• Decorative fonts

```html
<!DOCTYPE html>
<html lang="en">
<head>
<meta charset="utf-8">
<title>Dana Whitfield and Collaborators – Online Teaching Standards</title>
<link rel="stylesheet" href="https://fonts.googleapis.com/css2?family=Roboto:wght@300;400;700&family=Roboto+Condensed:wght@700&family=Crimson+Text:wght@400;700&display=swap">
<style>
  :root {
    --emerald: #2e9a6f;
    --ink: #2b2b2b;
    --heading-grey: #6d7f8c;
    --body-grey: #5a5a5a;
    --paper: #ffffff;
    --backdrop: #e6e9ea;
    --card: rgba(255, 255, 255, 0.74);
  }
  * { box-sizing: border-box; margin: 0; padding: 0; }
  html, body { width: 1200px; height: 1126px; overflow: hidden; background: var(--backdrop); }
  .poster {
    position: absolute; left: 220px; top: 26px;
    width: 746px; height: 1055px;
    background: var(--paper); overflow: hidden;
    font-family: "Roboto", "Helvetica Neue", Arial, sans-serif;
    color: var(--ink);
  }
  .poster-title { position: absolute; left: 34px; top: 70px; font-weight: 300; color: #2f2f2f; }
  .poster-title .name { display: block; font-size: 64px; line-height: 1; letter-spacing: -1.5px; }
  .poster-title .with { display: block; font-size: 38px; line-height: 1.2; margin-top: 8px; letter-spacing: -0.5px; }
  .brand { position: absolute; left: 503px; top: 80px; display: flex; align-items: center; gap: 12px; }
  .brand-mark { width: 38px; height: 38px; background: var(--emerald); }
  .brand-name { font-weight: 700; font-size: 12px; line-height: 1.3; color: var(--emerald); letter-spacing: 0.4px; text-transform: uppercase; }
  .band { position: absolute; left: 0; top: 228px; width: 100%; height: 106px; background: var(--emerald); }
  .photo {
    position: absolute; left: 0; top: 334px; width: 100%; height: 721px;
    background:
      radial-gradient(ellipse 220px 300px at 640px 560px, rgba(135,155,180,0.55), rgba(135,155,180,0) 80%),
      radial-gradient(ellipse 260px 220px at 230px 560px, rgba(205,175,155,0.4), rgba(205,175,155,0) 80%),
      linear-gradient(180deg, #f5f7f7 0%, #eef1f0 35%, #dcd6d0 70%, #bdb3aa 100%);
  }
  .column { position: absolute; top: 228px; width: 216px; }
  .col-1 { left: 29px; } .col-2 { left: 263px; } .col-3 { left: 497px; }
  .column-head { display: flex; align-items: flex-start; color: #fff; height: 50px; padding-top: 6px; }
  .column-head .num { font-weight: 700; font-size: 50px; line-height: 0.8; margin-right: 6px; letter-spacing: -2px; }
  .column-head .label { font-weight: 300; font-size: 24px; line-height: 1; }
  .column-intro { font-family: "Crimson Text", Georgia, serif; font-size: 9px; line-height: 1.2; color: #fff; margin-top: 2px; width: 220px; }
  .column-intro b { font-weight: 700; }
  .column-link {
    position: absolute; top: 90px; left: 0; height: 16px; padding: 3px 6px 0;
    background: #fff; border-radius: 4px 4px 0 0;
    font-size: 7.8px; font-weight: 700; color: #222; white-space: nowrap;
  }
  .cards { position: absolute; top: 112px; left: 0; width: 216px; background: var(--card); padding: 18px 6px 0; }
  .col-1 .cards { height: 642px; } .col-2 .cards { height: 486px; } .col-3 .cards { height: 245px; }
  .standard { height: 80px; }
  .standard h3 { font-family: "Roboto Condensed", "Arial Narrow", sans-serif; font-weight: 700; font-size: 12px; line-height: 1; color: var(--heading-grey); }
  .standard .lead { font-family: "Roboto Condensed", "Arial Narrow", sans-serif; font-size: 8px; font-weight: 700; line-height: 1.25; color: #1e1e1e; margin-top: 2px; }
  .standard .lead .arrow { color: var(--emerald); }
  .standard .detail { font-size: 7.4px; line-height: 1.35; color: var(--body-grey); margin-top: 3px; }
  .site-url { position: absolute; right: 36px; top: 1012px; font-weight: 700; font-size: 15px; color: #fff; }
</style>
</head>
<body>
<main class="poster">
  <h1 class="poster-title"><span class="name">Dana Whitfield</span><span class="with">and Collaborators</span></h1>
  <div class="brand"><span class="brand-mark"></span><span class="brand-name">Brightmeadow<br>Teaching<br>Standards</span></div>
  <div class="band"></div>
  <div class="photo" role="img" aria-label="Photograph of smiling university students working at a table with laptops"></div>

  <section class="column col-1">
    <h2 class="column-head"><span class="num">1</span><span class="label">Students</span></h2>
    <p class="column-intro">Students are supported in their online learning with a quality <b>curriculum</b> [1–4], opportunities for <b>interaction</b> with peers and staff [5&amp;6], and appropriate <b>support</b> [7&amp;8].</p>
    <div class="column-link">www.brightmeadowhub.org/standards/students/</div>
    <div class="cards">
      <article class="standard"><h3>1. Curriculum materials are aligned,<br>available and engaging</h3><p class="lead"><span class="arrow">➜</span> The necessary materials are constructively aligned and available online.</p><p class="detail">The materials are provided using a variety of media to engage students and support diversity.</p></article>
      <article class="standard"><h3>1. Curriculum materials are aligned,<br>available and engaging</h3><p class="lead"><span class="arrow">➜</span> The necessary materials are constructively aligned and available online.</p><p class="detail">The materials are provided using a variety of media to engage students and support diversity.</p></article>
      <article class="standard"><h3>1. Curriculum materials are aligned,<br>available and engaging</h3><p class="lead"><span class="arrow">➜</span> The necessary materials are constructively aligned and available online.</p><p class="detail">The materials are provided using a variety of media to engage students and support diversity.</p></article>
      <article class="standard"><h3>1. Curriculum materials are aligned,<br>available and engaging</h3><p class="lead"><span class="arrow">➜</span> The necessary materials are constructively aligned and available online.</p><p class="detail">The materials are provided using a variety of media to engage students and support diversity.</p></article>
      <article class="standard"><h3>1. Curriculum materials are aligned,<br>available and engaging</h3><p class="lead"><span class="arrow">➜</span> The necessary materials are constructively aligned and available online.</p><p class="detail">The materials are provided using a variety of media to engage students and support diversity.</p></article>
      <article class="standard"><h3>1. Curriculum materials are aligned,<br>available and engaging</h3><p class="lead"><span class="arrow">➜</span> The necessary materials are constructively aligned and available online.</p><p class="detail">The materials are provided using a variety of media to engage students and support diversity.</p></article>
      <article class="standard"><h3>1. Curriculum materials are aligned,<br>available and engaging</h3><p class="lead"><span class="arrow">➜</span> The necessary materials are constructively aligned and available online.</p><p class="detail">The materials are provided using a variety of media to engage students and support diversity.</p></article>
      <article class="standard"><h3>1. Curriculum materials are aligned,<br>available and engaging</h3><p class="lead"><span class="arrow">➜</span> The necessary materials are constructively aligned and available online.</p><p class="detail">The materials are provided using a variety of media to engage students and support diversity.</p></article>
    </div>
  </section>

  <section class="column col-2">
    <h2 class="column-head"><span class="num">2</span><span class="label">Staff</span></h2>
    <p class="column-intro">Students are supported in their online learning with a quality <b>curriculum</b> [1–4], opportunities for <b>interaction</b> with peers and staff [5&amp;6], and appropriate <b>support</b> [7&amp;8].</p>
    <div class="column-link">www.brightmeadowhub.org/standards/staff/</div>
    <div class="cards">
      <article class="standard"><h3>1. Curriculum materials are aligned,<br>available and engaging</h3><p class="lead"><span class="arrow">➜</span> The necessary materials are constructively aligned and available online.</p><p class="detail">The materials are provided using a variety of media to engage students and support diversity.</p></article>
      <article class="standard"><h3>1. Curriculum materials are aligned,<br>available and engaging</h3><p class="lead"><span class="arrow">➜</span> The necessary materials are constructively aligned and available online.</p><p class="detail">The materials are provided using a variety of media to engage students and support diversity.</p></article>
      <article class="standard"><h3>1. Curriculum materials are aligned,<br>available and engaging</h3><p class="lead"><span class="arrow">➜</span> The necessary materials are constructively aligned and available online.</p><p class="detail">The materials are provided using a variety of media to engage students and support diversity.</p></article>
      <article class="standard"><h3>1. Curriculum materials are aligned,<br>available and engaging</h3><p class="lead"><span class="arrow">➜</span> The necessary materials are constructively aligned and available online.</p><p class="detail">The materials are provided using a variety of media to engage students and support diversity.</p></article>
      <article class="standard"><h3>1. Curriculum materials are aligned,<br>available and engaging</h3><p class="lead"><span class="arrow">➜</span> The necessary materials are constructively aligned and available online.</p><p class="detail">The materials are provided using a variety of media to engage students and support diversity.</p></article>
      <article class="standard"><h3>1. Curriculum materials are aligned,<br>available and engaging</h3><p class="lead"><span class="arrow">➜</span> The necessary materials are constructively aligned and available online.</p><p class="detail">The materials are provided using a variety of media to engage students and support diversity.</p></article>
    </div>
  </section>

  <section class="column col-3">
    <h2 class="column-head"><span class="num">3</span><span class="label">Organisation</span></h2>
    <p class="column-intro">Students are supported in their online learning with a quality <b>curriculum</b> [1–4], opportunities for <b>interaction</b> with peers and staff [5&amp;6], and appropriate <b>support</b> [7&amp;8].</p>
    <div class="column-link">www.brightmeadowhub.org/standards/organisation/</div>
    <div class="cards">
      <article class="standard"><h3>1. Curriculum materials are aligned,<br>available and engaging</h3><p class="lead"><span class="arrow">➜</span> The necessary materials are constructively aligned and available online.</p><p class="detail">The materials are provided using a variety of media to engage students and support diversity.</p></article>
      <article class="standard"><h3>1. Curriculum materials are aligned,<br>available and engaging</h3><p class="lead"><span class="arrow">➜</span> The necessary materials are constructively aligned and available online.</p><p class="detail">The materials are provided using a variety of media to engage students and support diversity.</p></article>
      <article class="standard"><h3>1. Curriculum materials are aligned,<br>available and engaging</h3><p class="lead"><span class="arrow">➜</span> The necessary materials are constructively aligned and available online.</p><p class="detail">The materials are provided using a variety of media to engage students and support diversity.</p></article>
    </div>
  </section>

  <p class="site-url">www.brightmeadowhub.org</p>
</main>
</body>
</html>
```